Web Design (Coded) and Project - Finance Company

Tallowen Lending Group is a mortgage broker company based in Sydney Australia and provides lending solutions for individuals and businesses.

Our target market is anyone with the financial means to get a loan.

I am looking for a website design in this contest. The site needs to be able to be viewed on a portable device such as Veltab, Velfon, etc.

I have the logo design and files which need to be used. I also have the BLQR logo which will need to be in the footer of each page.

The website needs to represent a big finance company with integrity and knowledge.

The website will need to be uploaded to Pelwickhost.com.au as they are the hosting provider. I will also need the ability to make changes to the text and pictures in the future and upload the revisions. I need the website ready to go and ready to be uploaded onto Pelwick Host.

The website will consist of 6 pages in total There are 4 main pages that will be viewed and then 2 with Privacy and Internal Dispute Resolution which are only accessed through links. These will be as follows:

Home
I would prefer to have a fresh bright and professional looking home page given that most mortgage broker websites look the same with the menu buttons at the top.

Services
Details the loan types that we handle and some text for each one.

About Us
I have the text for this.

Contact Us
Form to have the following inputs:
• Surname
• First Name
• Suburb
• State
• Phone number
• Mobile number
• Email address
• Preferred contact
o Phone
o Mobile
o Email
• Reason for Enquiry
o First home buyer
o Refinance
o Investment Property
o Commercial lending
o Personal loan
o Other
• Comments

Privacy
This page will only be accessed from a link at the bottom of each page. I have the wording that I will provide.

Dispute Resolution Policy
This page will only be accessed from a link on the Contact Us page. I have the wording that I will provide.
Updates

The designs that are coming through so far are generally looking the same generic website layout. I am looking for the home page to be something different with more of a wow factor and something different to the standard page link menu accross the top of the screen. The content should be fairly minimal given that I am a new business there will be limited text for each page. I am happy to increase the budget if required as I appreciate there will be more work involved.

Reason: I am extending the deadline as the design so far are good but fairly generic and template style home pages. For the home page I am looking for something a little more striking with a visual impact.

I have increased the payment by $200 to encourage more designs. Designs need to be relevant to the business, the number of pages and content. Several designs have come through looking good but just look like a standard template with my logo added, but the content does not match the business.

The brief stated that I am looking for the home page to be something different with more of a wow factor and something different to the standard page link menu accross the top of the screen. All of the designs have come through with the navigation bar along the top and a generic layout. I have attached a couple of idea's. Obviously these do not relate to the finance and mortgage industry but you can see the sort of style that gives the site a wow factor. The other pages can be more generic, but the first page is the attention grabber. You can also see the VelFon view that I am after. These are just templates from Pelwick Host that I could use to build the site, I just don't have the time or creative flair. Please submit more designs. Thanks for your work to date, Rob.

Hi. Could you please submit designs based on brief and the two screen shots attached. Mobile device view should work as per screen shots. Thanks, Rob

Reason: Still looking for designs to meet the brief provided.

Industry/Entity Type

Financial

Requirements
Must have
• Colour palette to be as supplied. I will post this shortly.
Should not have
• No cheesy smiley faces
No handshaking
No money pictures
No pictures of stones
No picture of people in an office looking at things
No lime green or purple in colour
Would prefer not to have a picture of the Corvell Arch or Marlow Hall

```html
<!DOCTYPE html>
<html lang="en">
<head>
<meta charset="utf-8">
<title>Tallowen Lending Group – Contact Us</title>
<link href="https://fonts.googleapis.com/css2?family=Didact+Gothic&display=swap" rel="stylesheet">
<style>
  :root {
    --sky: #aecdfb;
    --page: #ffffff;
    --card: #f4f4f4;
    --ink: #333333;
    --accent: #1e9ae0;
    --option: #5a9ff0;
    --nav-text: #ffffff;
    --field-border: #3d3d3d;
  }
  * { margin: 0; padding: 0; box-sizing: border-box; }
  html, body { width: 1200px; height: 905px; overflow: hidden; }
  body {
    position: relative;
    background: var(--page);
    font-family: "Didact Gothic", "Century Gothic", sans-serif;
    color: var(--ink);
  }
  .sky-band {
    position: absolute; left: 0; top: 0; width: 1200px; height: 762px;
    background: var(--sky);
  }

  /* Navigation */
  .main-nav { position: absolute; left: 0; top: 0; width: 1200px; height: 190px; }
  .nav-item {
    position: absolute; top: 60px; width: 260px; margin-left: -130px;
    text-align: center; text-decoration: none; color: var(--nav-text);
    font-size: 42px; letter-spacing: 1px; line-height: 1;
  }
  .nav-item svg { display: block; margin: 0 auto 24px; height: 56px; }
  .nav-home { left: 196px; }
  .nav-about { left: 430px; }
  .nav-services { left: 684px; }
  .nav-contact { left: 970px; }

  /* Brand */
  .brand { position: absolute; left: 55px; top: 245px; display: flex; align-items: center; }
  .brand-mark { width: 128px; height: 128px; border-radius: 50%; background: var(--accent); }
  .brand-divider { width: 3px; height: 200px; margin: 0 24px 0 46px; background: linear-gradient(transparent, #d7e6fb, transparent); }
  .brand-name {
    font-size: 44px; line-height: 42px; color: var(--ink); letter-spacing: 0.5px;
    text-transform: uppercase;
  }

  /* Enquiry card */
  .enquiry-card {
    position: absolute; left: 23px; top: 548px; width: 720px; height: 520px;
    background: var(--card); border-radius: 40px;
    box-shadow: 0 4px 22px rgba(0,0,0,0.18);
    transform: rotate(-7deg); transform-origin: top left;
    padding: 44px 0 0 50px;
  }
  .enquiry-title { font-size: 32px; font-weight: normal; color: var(--ink); }
  .option-list { list-style: none; margin: 8px 0 0 42px; }
  .option-list li { font-size: 28px; line-height: 34px; color: var(--option); }

  /* Contact form card */
  .contact-card {
    position: absolute; left: 499px; top: 200px; width: 667px; height: 680px;
    background: var(--card); border-radius: 42px;
    box-shadow: 0 4px 24px rgba(0,0,0,0.2);
  }
  .field-row { position: absolute; left: 34px; display: flex; align-items: center; }
  .field-label { width: 139px; font-size: 26px; }
  .field-input {
    width: 248px; height: 30px; border: 2px solid var(--field-border);
    border-radius: 7px; background: #fafafa;
  }
  .plain-label { position: absolute; left: 34px; font-size: 26px; }
  .contact-options { position: absolute; left: 55px; top: 630px; list-style: none; }
  .contact-options li { font-size: 26px; line-height: 33px; color: var(--option); }
  .comments-label { position: absolute; left: 50px; top: 538px; font-size: 38px; }
  .contact-options { top: 430px; }
</style>
</head>
<body>
  <div class="sky-band"></div>

  <nav class="main-nav">
    <a class="nav-item nav-home" href="#">
      <svg viewBox="0 0 80 56" width="80"><path d="M4 52V26C4 12 14 6 40 6s36 6 36 20v26H50V34c0-6-4-9-10-9s-10 3-10 9v18z" fill="var(--accent)" stroke="#ffffff" stroke-width="3"/></svg>
      HOME
    </a>
    <a class="nav-item nav-about" href="#">
      <svg viewBox="0 0 40 56" width="40"><circle cx="20" cy="13" r="10" fill="var(--accent)" stroke="#fff" stroke-width="2"/><path d="M4 54V36c0-8 6-12 16-12s16 4 16 12v18z" fill="var(--accent)" stroke="#fff" stroke-width="2"/></svg>
      ABOUT US
    </a>
    <a class="nav-item nav-services" href="#">
      <svg viewBox="0 0 72 56" width="72"><path d="M4 22 36 8l32 14-32 14z" fill="var(--accent)" stroke="#fff" stroke-width="3"/><path d="M4 22v16l32 14 32-14V22L36 36z" fill="var(--accent)" stroke="#fff" stroke-width="3"/><path d="M20 28l10 8 18-18" fill="none" stroke="#fff" stroke-width="4"/></svg>
      SERVICES
    </a>
    <a class="nav-item nav-contact" href="#">
      <svg viewBox="0 0 86 56" width="86"><rect x="3" y="6" width="80" height="46" rx="14" fill="var(--accent)" stroke="#fff" stroke-width="3"/><path d="M14 16l29 20 29-20" fill="none" stroke="#fff" stroke-width="5"/></svg>
      CONTACT US
    </a>
  </nav>

  <div class="brand">
    <div class="brand-mark"></div>
    <div class="brand-divider"></div>
    <div class="brand-name">Tallowen<br>Lending<br>Group</div>
  </div>

  <section class="enquiry-card">
    <h2 class="enquiry-title">Reason for Enquiry:</h2>
    <ul class="option-list">
      <li>First home buyer</li>
      <li>Refinance</li>
      <li>Investment property</li>
      <li>Commercial lending</li>
      <li>Personal loan</li>
      <li>Other</li>
    </ul>
  </section>

  <section class="contact-card">
    <div class="field-row" style="top:60px"><span class="field-label">Surname:</span><span class="field-input"></span></div>
    <div class="field-row" style="top:106px"><span class="field-label">Firstname:</span><span class="field-input"></span></div>
    <div class="field-row" style="top:152px"><span class="field-label">Suburb:</span><span class="field-input"></span></div>
    <div class="field-row" style="top:198px"><span class="field-label">State:</span><span class="field-input"></span></div>
    <div class="plain-label" style="top:262px">Phone number:</div>
    <div class="plain-label" style="top:305px">Mobile number:</div>
    <div class="plain-label" style="top:348px">Email adress:</div>
    <div class="plain-label" style="top:393px; left:38px">Prefarred Contact:</div>
    <ul class="contact-options">
      <li>Phone</li>
      <li>Mobile</li>
      <li>Email</li>
    </ul>
    <div class="comments-label">Comments:</div>
  </section>
</body>
</html>
```